Harbor Lane Group Bus Card Design

We need a business card for our law firm that specializes in intellectual property law (patents, trademarks, copyrights). We are called The Harbor Lane Group. We have a globe logo (attached) that is currently the back of our card. We like the back, but aren't married to it. I will also attach the front side of what we use now. The black background looks bad/cheap. We want something that looks sharp and modern. Thank you.

```html
<!DOCTYPE html>
<html lang="en">
<head>
<meta charset="utf-8">
<title>The Harbor Lane Group – Business Card</title>
<link rel="stylesheet" href="https://fonts.googleapis.com/css2?family=Lato:wght@300;400;700;900&display=swap">
<style>
  :root {
    --page-bg: #eef0f2;
    --brand-blue: #5fa8de;
    --brand-blue-deep: #5a97cc;
    --brand-blue-light: #7bb6e6;
    --card-white: #ffffff;
    --card-grey: #d9d9d9;
    --ink: #1b1b1b;
    --text-light: #ffffff;
    --text-soft: #e6f2fb;
  }
  * { box-sizing: border-box; margin: 0; padding: 0; }
  html, body {
    width: 1200px;
    height: 900px;
    overflow: hidden;
  }
  body {
    background: var(--page-bg);
    font-family: "Lato", Arial, sans-serif;
    display: flex;
    align-items: center;
    justify-content: center;
    gap: 40px;
  }
  .card {
    width: 540px;
    height: 309px;
    position: relative;
    overflow: hidden;
    box-shadow: 0 6px 18px rgba(0, 0, 0, 0.18);
  }

  /* Brand lockup */
  .brand {
    display: flex;
    flex-direction: column;
    align-items: center;
  }
  .brand-line {
    display: flex;
    align-items: center;
    gap: 10px;
  }
  .brand-dot {
    width: 26px;
    height: 26px;
    border-radius: 50%;
    background: var(--brand-blue-light);
  }
  .brand-name {
    font-weight: 900;
    font-size: 22px;
    letter-spacing: 0.5px;
    color: var(--ink);
    text-transform: uppercase;
  }
  .brand-services {
    margin-top: 6px;
    font-weight: 700;
    font-size: 10.5px;
    letter-spacing: 1.2px;
    text-transform: uppercase;
    color: var(--ink);
  }

  /* Back face */
  .card-back {
    background: radial-gradient(ellipse at 40% 30%, var(--brand-blue-light) 0%, var(--brand-blue-deep) 75%);
    display: flex;
    flex-direction: column;
    align-items: center;
    justify-content: center;
  }
  .card-back .brand-name { font-size: 20px; }
  .back-website {
    margin-top: 28px;
    font-weight: 700;
    font-size: 10.5px;
    letter-spacing: 1px;
    color: var(--ink);
  }

  /* Front face */
  .card-front { background: var(--card-white); }
  .front-top {
    position: absolute;
    inset: 0 0 auto 0;
    height: 150px;
    background: linear-gradient(180deg, #ffffff 0%, #f1f1f1 100%);
    display: flex;
    align-items: center;
    justify-content: center;
    padding-top: 10px;
  }
  .front-band {
    position: absolute;
    left: 0;
    right: 0;
    top: 150px;
    height: 125px;
    background: var(--brand-blue);
    display: flex;
    align-items: center;
    padding: 0 30px;
  }
  .front-strip {
    position: absolute;
    left: 0;
    right: 0;
    bottom: 0;
    height: 34px;
    background: var(--card-grey);
  }
  .person {
    width: 235px;
    text-align: center;
    color: var(--text-light);
  }
  .person-name { font-size: 24px; font-weight: 400; }
  .person-title { font-size: 15px; font-weight: 300; color: var(--text-soft); margin-top: 2px; }
  .person-address { font-size: 16px; font-weight: 300; margin-top: 8px; line-height: 1.25; }
  .contact-list {
    list-style: none;
    margin-left: 25px;
    color: var(--text-light);
    font-size: 14.5px;
    font-weight: 300;
  }
  .contact-item {
    display: flex;
    align-items: center;
    gap: 9px;
    line-height: 1.55;
  }
  .contact-icon { width: 16px; height: 16px; flex: none; }
</style>
</head>
<body>

  <section class="card card-back" aria-label="Card back">
    <div class="brand">
      <div class="brand-line">
        <span class="brand-dot"></span>
        <span class="brand-name">The Harbor Lane Group</span>
      </div>
      <p class="brand-services">Patents | Copyrights | Trademarks</p>
    </div>
    <p class="back-website">www.HarborLaneGroup.com</p>
  </section>

  <section class="card card-front" aria-label="Card front">
    <div class="front-top">
      <div class="brand">
        <div class="brand-line">
          <span class="brand-dot"></span>
          <span class="brand-name">The Harbor Lane Group</span>
        </div>
        <p class="brand-services">Patents | Copyrights | Trademarks</p>
      </div>
    </div>

    <div class="front-band">
      <div class="person">
        <p class="person-name">John Smith</p>
        <p class="person-title">Managing Director</p>
        <p class="person-address">1234, Address GoesHere<br>Country, 12345</p>
      </div>

      <ul class="contact-list">
        <li class="contact-item">
          <svg class="contact-icon" viewBox="0 0 16 16" aria-hidden="true">
            <rect width="16" height="16" rx="2" fill="#fff"/>
            <path d="M4 5.5c0-1 1-1.5 4-1.5s4 .5 4 1.5v1H10V5.6H6v.9H4z M5 8h6l1 4H4z" fill="#5fa8de"/>
          </svg>
          <span>123-456-7890</span>
        </li>
        <li class="contact-item">
          <svg class="contact-icon" viewBox="0 0 16 16" aria-hidden="true">
            <rect width="16" height="16" rx="2" fill="#fff"/>
            <rect x="4" y="3" width="8" height="4" fill="#5fa8de"/>
            <rect x="3" y="7" width="10" height="6" rx="1" fill="#5fa8de"/>
          </svg>
          <span>123-456-7890</span>
        </li>
        <li class="contact-item">
          <svg class="contact-icon" viewBox="0 0 16 16" aria-hidden="true">
            <rect width="16" height="16" rx="2" fill="#fff"/>
            <rect x="3" y="4.5" width="10" height="7" fill="#5fa8de"/>
            <path d="M3 4.5l5 4 5-4" fill="none" stroke="#fff" stroke-width="1.2"/>
          </svg>
          <span>info@youremail.com</span>
        </li>
        <li class="contact-item">
          <svg class="contact-icon" viewBox="0 0 16 16" aria-hidden="true">
            <rect width="16" height="16" rx="2" fill="#fff"/>
            <path d="M6.5 9.5l3-3 M7.5 5l1-1a2 2 0 0 1 3 3l-1 1 M8.5 11l-1 1a2 2 0 0 1-3-3l1-1" fill="none" stroke="#5fa8de" stroke-width="1.4" stroke-linecap="round"/>
          </svg>
          <span>www.yourweb.com</span>
        </li>
      </ul>
    </div>

    <div class="front-strip"></div>
  </section>

</body>
</html>
```